New Business Card Design*

We are a recruitment company based in Norwich/Cambridge England.
I have included our company logo which we want to remain the same.

What we are looking for is a new creative Business card which will really stand out!!

Contact Information for Business Card

Harriet Vance
email: Harriet@brelvix.co.uk
Address: Tolworth House
Ashgrove Innovation Park
Pelham Road
Norwich
KT9 3QD
Tel:01632 960418

```html
<!DOCTYPE html>
<html lang="en">
<head>
<meta charset="utf-8">
<title>Brelvix Business Card</title>
<link rel="stylesheet" href="https://fonts.googleapis.com/css2?family=Arimo:wght@400;700&display=swap">
<style>
  :root {
    --page-bg: #d9d4cc;
    --card-top: #f3f4f3;
    --card-bottom: #e3e6e4;
    --ink-grey: #55555d;
    --ink-text: #5f6066;
    --brand-green: #56a332;
    --band-grey: #56545e;
    --edge-white: #ffffff;
  }
  * { margin: 0; padding: 0; box-sizing: border-box; }
  html, body {
    width: 1200px;
    height: 970px;
    overflow: hidden;
    background: var(--page-bg);
    font-family: "Arimo", Arial, sans-serif;
  }
  .business-card {
    position: absolute;
    left: 100px;
    top: 200px;
    width: 1000px;
    height: 570px;
    background: linear-gradient(160deg, var(--card-top), var(--card-bottom));
    overflow: hidden;
    box-shadow: 0 10px 30px rgba(0,0,0,0.18);
  }
  .side-sweep {
    position: absolute;
    inset: 0;
    width: 1000px;
    height: 570px;
  }
  .brand {
    position: absolute;
    left: 62px;
    top: 66px;
    display: flex;
    align-items: center;
  }
  .brand-dot {
    width: 132px;
    height: 132px;
    border-radius: 50%;
    background: var(--brand-green);
    margin-right: 66px;
  }
  .brand-name {
    font-weight: 700;
    font-size: 82px;
    line-height: 1;
    color: var(--ink-grey);
    letter-spacing: -1px;
  }
  .brand-tagline {
    position: absolute;
    left: 262px;
    top: 186px;
    font-weight: 700;
    font-size: 15px;
    letter-spacing: 4.4px;
    color: var(--ink-grey);
  }
  .person {
    position: absolute;
    left: 60px;
    top: 277px;
  }
  .person-name {
    font-weight: 700;
    font-size: 33px;
    line-height: 1;
    color: var(--brand-green);
  }
  .person-role {
    font-size: 25px;
    line-height: 1;
    margin-top: 2px;
    color: var(--ink-text);
  }
  .address {
    position: absolute;
    left: 60px;
    top: 365px;
    font-size: 25px;
    line-height: 32px;
    color: var(--ink-text);
  }
  .contact-list {
    position: absolute;
    left: 56px;
    top: 441px;
    list-style: none;
  }
  .contact-list li {
    display: flex;
    align-items: center;
    height: 34px;
    font-size: 25px;
    color: var(--ink-text);
  }
  .contact-icon {
    width: 29px;
    height: 29px;
    margin-right: 12px;
    flex: none;
  }
</style>
</head>
<body>
  <div class="business-card">
    <svg class="side-sweep" viewBox="0 0 1000 570" aria-hidden="true">
      <defs>
        <linearGradient id="greenFill" x1="0" y1="0" x2="0" y2="1">
          <stop offset="0" stop-color="#5fae3b"/>
          <stop offset="1" stop-color="#3e871d"/>
        </linearGradient>
      </defs>
      <path d="M640 0 L800 0 C880 80 893 190 890 300 C860 150 780 50 640 0 Z" fill="var(--band-grey)"/>
      <path d="M805 0 C925 110 935 330 812 570 L1000 570 L1000 0 Z" fill="url(#greenFill)" stroke="var(--edge-white)" stroke-width="5"/>
    </svg>

    <div class="brand">
      <div class="brand-dot"></div>
      <div class="brand-name">Brelvix</div>
    </div>
    <div class="brand-tagline">Technology Recruitment</div>

    <div class="person">
      <div class="person-name">Harriet Vance</div>
      <div class="person-role">CEO</div>
    </div>

    <div class="address">
      Tolworth House, Ashgrove Innovation Park<br>
      Pelham Road, Norwich KT9 3QD
    </div>

    <ul class="contact-list">
      <li>
        <svg class="contact-icon" viewBox="0 0 30 30" aria-hidden="true">
          <circle cx="15" cy="15" r="13" fill="none" stroke="var(--brand-green)" stroke-width="2.5"/>
          <rect x="10.5" y="7.5" width="9" height="15" rx="1.5" fill="none" stroke="var(--brand-green)" stroke-width="2"/>
        </svg>
        01632 960418
      </li>
      <li>
        <svg class="contact-icon" viewBox="0 0 30 30" aria-hidden="true">
          <circle cx="15" cy="15" r="14" fill="var(--brand-green)"/>
          <rect x="8" y="10" width="14" height="10" fill="none" stroke="#fff" stroke-width="1.8"/>
          <path d="M8 10 L15 16 L22 10" fill="none" stroke="#fff" stroke-width="1.8"/>
        </svg>
        Harriet@brelvix.co.uk
      </li>
      <li>
        <svg class="contact-icon" viewBox="0 0 30 30" aria-hidden="true">
          <circle cx="15" cy="15" r="14" fill="var(--brand-green)"/>
          <circle cx="15" cy="15" r="8" fill="none" stroke="#fff" stroke-width="1.6"/>
          <ellipse cx="15" cy="15" rx="3.5" ry="8" fill="none" stroke="#fff" stroke-width="1.4"/>
          <path d="M7 15 H23" stroke="#fff" stroke-width="1.4"/>
        </svg>
        www.brelvix.co.uk
      </li>
    </ul>
  </div>
</body>
</html>
```